Flyer needed for Seminar

Hello,
We are looking for eye-catching, inspiring marketing material for an educational seminar. We need 4 x 6 clubcards with the following info:

CLUBCARD FRONT:

Verander Academy Presents:

Stillness: Under The Surface
Unlock the hidden treasures of prayer
By. Shaykh Idris Kamal Al-Furati

Dates:Jan 23-25, 2015
Timings: Fri - 7pm - 9:30 pm; Sat/Sun - 9am - 8 pm

Location: Riverbend Grand Suites at Oakhaven Square
4385 Millbrook Lane, Plano, TX 75093

Seating is Limited. Register Today!
www.VeranderAcademy,com

CLUBCARD BACK:
In this unique seminar, learn how to connect spiritually with your Creator through prayer. Let us teach you the hidden meanings behind salah and why it is essential to your existence. Not only will the instructor impart the skills you'll need to master khushoo but he will delve more deeply, into the inner realms and intricacies of this ibadaa. As a result, the prayer will no longer be regarded as a mechanical chore, but an intimate meeting with the Divine. Through such insight, we hope you will leave this non-fiqh seminar with an awakened and unparalleled understanding of this fundamental pillar of Islam.

www.VeranderAcademy.com
For more info: Email - info@veranderacademy.com; Phone - 1-877-Verand4

Reason: I really appreciate all the submissions but am looking for something more eye-catching, something that really stirs ones interest and relates to the title of the seminar. Thank you!

```html
<!DOCTYPE html>
<html lang="en">
<head>
<meta charset="utf-8">
<title>Stillness: Under The Surface — Seminar Clubcard</title>
<link rel="stylesheet" href="https://fonts.googleapis.com/css2?family=Cinzel:wght@500;700&family=Cormorant+Garamond:ital,wght@0,600;1,600&family=Arimo:wght@400;700&display=swap">
<style>
  :root {
    --page: #ffffff;
    --card-dark: #1b1e25;
    --card-back: #262a32;
    --gold: #d9b25a;
    --gold-light: #f6e3a1;
    --gold-deep: #a9792a;
    --white: #ffffff;
    --badge-ink: #5b1d0c;
    --icon-brown: #8a5636;
    --glow: #9fd3ff;
  }
  * { margin: 0; padding: 0; box-sizing: border-box; }
  html, body { width: 869px; height: 1200px; overflow: hidden; background: var(--page); }
  .canvas { position: relative; width: 869px; height: 1200px; background: var(--page); font-family: "Arimo", Arial, sans-serif; }

  .card { position: absolute; left: 0; width: 869px; }
  .card-front { top: 0; height: 579px; background: var(--card-dark); overflow: hidden; }
  .card-back { top: 619px; height: 581px; background: var(--card-back); border: 1px solid #9a9a9a; }

  .hero-art {
    position: absolute; left: 0; top: 0; width: 470px; height: 500px;
    background:
      radial-gradient(ellipse 170px 150px at 270px 200px, rgba(255,255,255,0.95), rgba(190,225,255,0.6) 40%, rgba(60,110,170,0.25) 75%, rgba(27,30,37,0) 100%),
      radial-gradient(ellipse 260px 300px at 260px 180px, rgba(70,120,180,0.55), rgba(27,30,37,0) 80%);
  }

  .ornament-top { position: absolute; left: 600px; top: 0; width: 140px; height: 36px; }

  .title { position: absolute; left: 480px; top: 92px; width: 380px; text-align: center; }
  .title-main {
    font-family: "Cinzel", serif; font-weight: 700; font-size: 48px; letter-spacing: 4px; line-height: 1;
    background: linear-gradient(180deg, var(--gold-light), var(--gold) 55%, var(--gold-deep));
    -webkit-background-clip: text; background-clip: text; color: transparent;
  }
  .title-sub {
    margin-top: 16px; font-family: "Cinzel", serif; font-weight: 500; font-size: 21px; letter-spacing: 1px;
    color: var(--gold);
  }
  .tagline-frame { position: absolute; left: 490px; top: 226px; width: 340px; height: 62px; }
  .tagline {
    position: absolute; left: 490px; top: 228px; width: 340px; text-align: center;
    font-family: "Cormorant Garamond", serif; font-weight: 600; font-size: 22px; line-height: 28px; color: var(--gold);
  }
  .speaker { position: absolute; left: 480px; top: 304px; width: 380px; text-align: center; font-weight: 700; font-size: 18px; color: var(--white); }
  .ornament-rule { position: absolute; left: 500px; top: 340px; width: 320px; height: 18px; }

  .schedule { position: absolute; left: 480px; top: 372px; width: 350px; text-align: center; font-weight: 700; font-size: 14.5px; line-height: 19px; color: var(--white); }

  .venue { position: absolute; left: 94px; top: 496px; display: flex; gap: 10px; }
  .venue-pin { width: 24px; height: 24px; flex: none; }
  .venue-text { font-weight: 700; font-size: 15px; line-height: 24px; color: var(--white); }

  .badge { position: absolute; }
  .badge svg { position: absolute; inset: 0; width: 100%; height: 100%; }
  .badge-text { position: absolute; inset: 0; display: flex; align-items: center; justify-content: center; text-align: center; font-weight: 700; color: var(--badge-ink); }
  .badge-front { left: 584px; top: 454px; width: 140px; height: 80px; }
  .badge-front .badge-text { font-size: 13.5px; line-height: 17px; }
  .badge-back { left: 114px; top: 347px; width: 214px; height: 106px; }
  .badge-back .badge-text { font-size: 17.5px; line-height: 22px; }

  .description {
    position: absolute; left: 94px; top: 80px; width: 682px;
    font-size: 15.3px; line-height: 25.5px; color: var(--white); text-align: justify;
  }
  .contact { position: absolute; left: 370px; top: 312px; }
  .contact-heading { margin-left: 51px; font-weight: 700; font-size: 26px; color: var(--white); margin-bottom: 10px; }
  .contact-row { display: flex; align-items: center; gap: 15px; height: 47px; font-weight: 700; font-size: 25px; color: var(--white); }
  .contact-icon { width: 36px; height: 36px; flex: none; }
</style>
</head>
<body>
<div class="canvas">
  <svg width="0" height="0" style="position:absolute">
    <defs>
      <linearGradient id="badgeGold" x1="0" y1="0" x2="0" y2="1">
        <stop offset="0" stop-color="#fbe9a6"/>
        <stop offset="0.5" stop-color="#e6bd4f"/>
        <stop offset="1" stop-color="#b98325"/>
      </linearGradient>
      <symbol id="starburst" viewBox="0 0 200 100" preserveAspectRatio="none">
        <polygon fill="url(#badgeGold)" points="198,50 184.4,57.8 190.6,68.4 171.5,72.2 169.3,83.9 147.8,83.2 137.5,94.4 116.8,89.2 100,98 83.2,89.2 62.5,94.4 52.2,83.2 30.7,83.9 28.5,72.2 9.4,68.4 15.6,57.8 2,50 15.6,42.2 9.4,31.6 28.5,27.8 30.7,16.1 52.2,16.8 62.5,5.6 83.2,10.8 100,2 116.8,10.8 137.5,5.6 147.8,16.8 169.3,16.1 171.5,27.8 190.6,31.6 184.4,42.2"/>
      </symbol>
    </defs>
  </svg>

  <section class="card card-front">
    <div class="hero-art" role="img" aria-label="Open cupped hands raised in prayer beneath a glowing crescent and star, set in soft blue light"></div>

    <svg class="ornament-top" viewBox="0 0 140 36"><path d="M10 30 H130" stroke="var(--gold)" stroke-width="2"/><rect x="62" y="6" width="16" height="16" transform="rotate(45 70 14)" fill="var(--gold)"/></svg>

    <div class="title">
      <div class="title-main">STILLNESS</div>
      <div class="title-sub">UNDER THE SURFACE</div>
    </div>

    <svg class="tagline-frame" viewBox="0 0 340 62"><path d="M2 2 H338 M2 60 H338" stroke="var(--gold)" stroke-width="1.5" fill="none"/></svg>
    <div class="tagline">Unlock the hidden<br>treasures of prayer</div>

    <div class="speaker">By. Shaykh Idris Kamal Al-Furati</div>
    <svg class="ornament-rule" viewBox="0 0 320 18"><path d="M0 9 H145 M175 9 H320" stroke="var(--gold)" stroke-width="1.5"/><circle cx="160" cy="9" r="5" fill="var(--gold)"/></svg>

    <div class="schedule">Dates:Jan 23-25, 2015<br>Timings: Fri - 7pm - 9:30 pm;<br>Sat/Sun - 9am - 8 pm</div>

    <div class="badge badge-front">
      <svg><use href="#starburst"/></svg>
      <div class="badge-text">Seating is Limited.<br>Register Today!</div>
    </div>

    <div class="venue">
      <svg class="venue-pin" viewBox="0 0 24 24"><circle cx="12" cy="12" r="12" fill="var(--icon-brown)"/><path d="M12 5 a4.5 4.5 0 0 1 4.5 4.5 c0 3.5 -4.5 8.5 -4.5 8.5 s-4.5 -5 -4.5 -8.5 A4.5 4.5 0 0 1 12 5z" fill="#f3e2c8"/><circle cx="12" cy="9.5" r="1.8" fill="var(--icon-brown)"/></svg>
      <div class="venue-text">Riverbend Grand Suites at Oakhaven Square<br>&nbsp;&nbsp;&nbsp;4385 Millbrook Lane, Plano, TX 75093</div>
    </div>
  </section>

  <section class="card card-back">
    <p class="description">In this unique seminar, learn how to connect spiritually with your Creator through prayer. Let us teach you the hidden meanings behind salah and why it is essential to your existence. Not only will the instructor impart the skills you'll need to master khushoo but he will delve more deeply, into the inner realms and intricacies of this ibadaa. As a result, the prayer will no longer be regarded as a mechanical chore, but an intimate meeting with the Divine. Through such insight, we hope you will leave this non-fiqh seminar with an awakened and unparalleled understanding of this fundamental pillar of Islam.</p>

    <div class="badge badge-back">
      <svg><use href="#starburst"/></svg>
      <div class="badge-text">Seating is Limited.<br>Register Today!</div>
    </div>

    <div class="contact">
      <div class="contact-heading">For more info:</div>
      <div class="contact-row">
        <svg class="contact-icon" viewBox="0 0 36 36"><circle cx="18" cy="18" r="18" fill="var(--icon-brown)"/><rect x="9" y="12" width="18" height="12" fill="#f3e2c8"/><path d="M9 12 L18 19 L27 12" stroke="var(--icon-brown)" stroke-width="1.6" fill="none"/></svg>
        <span>info@veranderacademy.com;</span>
      </div>
      <div class="contact-row">
        <svg class="contact-icon" viewBox="0 0 36 36"><circle cx="18" cy="18" r="18" fill="var(--icon-brown)"/><g stroke="#f3e2c8" stroke-width="1.6" fill="none"><circle cx="18" cy="18" r="9"/><ellipse cx="18" cy="18" rx="4" ry="9"/><path d="M9 18 H27 M11 13 H25 M11 23 H25"/></g></svg>
        <span>www.VeranderAcademy.com</span>
      </div>
      <div class="contact-row">
        <svg class="contact-icon" viewBox="0 0 36 36"><circle cx="18" cy="18" r="18" fill="var(--icon-brown)"/><path d="M9 15 q9 -7 18 0 l-2 3 l-4 -1 v-2 h-6 v2 l-4 1z" fill="#f3e2c8"/><rect x="12" y="19" width="12" height="7" rx="1.5" fill="#f3e2c8"/><circle cx="18" cy="22.5" r="2" fill="var(--icon-brown)"/></svg>
        <span>1-877-Verand4</span>
      </div>
    </div>
  </section>
</div>
</body>
</html>
```